Biz card for my counselling/social work practice

Biz card design for my counselling practice, focus on well-being, I am a social worker who also teaches meditation and workshops but my main focus for the card is my counselling practice. My website reveals a gentle flowing quality which I would life reflected in my card. This business card will be designed to share with other practitioners who are looking for support with their clients to take their healing to another level or well-being.

Target Market(s)

professionals seeking mental health counselling/men/women/ those seeking to improve their well-being through insight based counselling to optimize their lives and process trauma or limiting patterns

Industry/Entity Type

Counsellor

Contact Information for Business Card

Info on the card: perhaps text is aligned left?
Maribel Strand, MSW, RSW
Counsellor
614.295.3140
info@maribelstrand.example
www.maribelstrand.example

Please use a modern font doesn’t need to be the one chosen below. Thank you

Font styles to use
Serif

Colors
3176b5
33a6d7
33b8a4
6b449b
abd037
d2a4cc
e55fa2

Requirements
Must have
• My business card details on front
• Backside
• Accelerated Resolution Therapy
• Cognitive Behavioral Therapy
• Mindfulness Informed Therapy
Nice to have
• I would like the card to be basic, (white or creme without too much bold colour) and with perhaps a stripe or band of vertical colour in blue or green (or a merge of colour) perhaps embossed or in a negative space. (this is one idea, but do not want the card to be too feminine or interest only women as i see men too so this is only an idea, but not 100 percent on this.
• I do not have a logo. I would prefer to heart from my website not to be used in the design as i am considering modifying this and re-branding.
Should not have
• too bold colours or bright yellow/blacks. i Like tones that are greens, blues.

```html
<!DOCTYPE html>
<html lang="en">
<head>
<meta charset="utf-8">
<title>Maribel Strand — Business Card</title>
<link href="https://fonts.googleapis.com/css2?family=Lato:ital,wght@0,400;0,700;0,900;1,400&display=swap" rel="stylesheet">
<style>
  :root {
    --teal: #256177;
    --teal-dark: #1d5368;
    --ink: #3a3f44;
    --paper: #ffffff;
    --stage: #2b2b2d;
  }
  * { margin: 0; padding: 0; box-sizing: border-box; }
  html, body { width: 1200px; height: 878px; overflow: hidden; }
  body {
    background: var(--stage);
    font-family: "Lato", sans-serif;
    display: flex;
    flex-direction: column;
    align-items: center;
    justify-content: center;
    gap: 40px;
  }
  .card {
    width: 630px;
    height: 360px;
    position: relative;
    box-shadow: 0 10px 30px rgba(0,0,0,.45);
  }
  .card-back { background: var(--teal); }
  .services {
    position: absolute;
    left: 48px;
    bottom: 44px;
    list-style: none;
    color: #fff;
    font-size: 21px;
    line-height: 1.45;
  }
  .card-front { background: var(--paper); }
  .identity { position: absolute; left: 48px; top: 44px; }
  .name {
    color: var(--teal);
    font-weight: 900;
    font-size: 34px;
    letter-spacing: -0.5px;
    line-height: 1;
  }
  .name .credentials { font-size: 21px; font-weight: 900; letter-spacing: 0; }
  .title {
    color: var(--ink);
    font-size: 18px;
    letter-spacing: 4px;
    margin-top: 4px;
  }
  .contact {
    position: absolute;
    left: 48px;
    bottom: 44px;
    list-style: none;
    color: var(--ink);
    font-style: italic;
    font-size: 22px;
    line-height: 1.45;
  }
  .contact li { display: flex; align-items: center; gap: 14px; }
  .contact svg { width: 20px; height: 20px; fill: var(--teal); flex: none; }
  .brand-mark {
    position: absolute;
    right: 44px;
    bottom: 70px;
    display: flex;
    align-items: center;
    gap: 12px;
    color: var(--teal);
    font-weight: 700;
    font-size: 24px;
  }
  .brand-mark .dot {
    width: 44px; height: 44px;
    border-radius: 50%;
    background: var(--teal);
  }
</style>
</head>
<body>
  <section class="card card-back">
    <ul class="services">
      <li>-Accelerated Resolution Therapy</li>
      <li>-Cognitive Behavioral Therapy</li>
      <li>-Mindfulness Informed Therapy</li>
    </ul>
  </section>

  <section class="card card-front">
    <div class="identity">
      <h1 class="name">Maribel Strand, <span class="credentials">MSW, RSW</span></h1>
      <p class="title">Counsellor</p>
    </div>

    <ul class="contact">
      <li>
        <svg viewBox="0 0 24 24" aria-hidden="true"><path d="M6.6 10.8a15.1 15.1 0 0 0 6.6 6.6l2.2-2.2c.3-.3.7-.4 1-.2 1.1.4 2.3.6 3.6.6.6 0 1 .4 1 1V20c0 .6-.4 1-1 1A17 17 0 0 1 3 4c0-.6.4-1 1-1h3.5c.6 0 1 .4 1 1 0 1.3.2 2.5.6 3.6.1.3 0 .7-.2 1z"/></svg>
        614.295.3140
      </li>
      <li>
        <svg viewBox="0 0 24 24" aria-hidden="true"><path d="M2 5h20v14H2z M3.5 6.5 12 13l8.5-6.5" stroke="#fff" stroke-width="1.4"/></svg>
        info@maribelstrand.example
      </li>
      <li>
        <svg viewBox="0 0 24 24" aria-hidden="true"><circle cx="12" cy="12" r="10"/><path d="M2 12h20M12 2c3 3 3 17 0 20M12 2c-3 3-3 17 0 20M4 7h16M4 17h16" stroke="#fff" stroke-width="1" fill="none"/></svg>
        www.maribelstrand.example
      </li>
    </ul>

    <div class="brand-mark">
      <span class="dot"></span>
      <span>Maribel Strand</span>
    </div>
  </section>
</body>
</html>
```